Brisk Mist Premium Cooling Towel

Similar to Tan Goat, Vantrel and Pebble. Brisk Mist's Products are a premium brand within the cooling market. From towels to high performance sports products Brisk Mists products crush the competitors. The product regardless of the conditions stays cold even in the hottest conditions. Our current clients range from the Grand Lanterns, Hollis Merrow's to professional athletes. We are currently redesigning our packaging for our towel line.

The goal of this design is to have someone look at the package and say "Whoa...". When customers first try the product they have a good idea of what to expect, then they try it and are blown away. Simply put the towel sells itself. Sales reps have stated that the highest closing rates are when they say nothing at all.

With that being said we are looking for a packaging that has the same effect. Imagine you are sitting by the pool side in Miami in the middle of the summer, you feel like your body is on fire. Someone then offers you a brisk mist towel that instantly cools you making the unbearable suddenly... enjoyable.

Yes, this is the effect we are looking for off the shelf. If this were on the shelf at Shopvale in the container how do we get this same effect. Things that our customers have indicated were a plus was when the cooling effect was displayed by both color and transition of the logo. This effect typically takes some layering in photo shop but when done right results in a much higher customer rating.

The containers are a plastic tube (roughly 10 inch by 3 inch in by diameter) and an envelope style pouch that is 10inch by 6inch. Official dimensions will be updated later this week.

We are looking for a simple clean look that screams "premium". Again, the "whoa" factor is a must to stand out against competitors. The main color schemes to consider are hot red, Ice cold blue, silver, black. Realizing that building a a compelling design that relates to an audience of 16-30 Male and Female is tough please ask questions. It must connect to parents, teens and active athletes. Again, think Tan Goat and how it connects with everyone.

Competitors:
1. http://www.buildkitdepot.example/brix-lane-breezy-sport-cooling-towel.html?id=10293847560

2.http://www.valuebarnoutlet.example/product/3-4418290?ref=shop

3. http://www.marketrivo.example/Quest-Steadyfrost-Instant-Cooling-Towel/dp/Q7TR2LMX40/ref=sim_2

4. http://www.frostwrapz.example/

5. http://www.halvorwear.example/Tera-Glaze-Cooling-Performance-Clothing-Apparel/Technology_Tera-Glaze_Nil,default,pg.html

6. http://www.searchloom.example/shopping/pine-ridge-outfitters-harbor-hawks-cooling-towel-white-5503811/p/C7DA19F0A3B2?q=cooling+towel

7. http://www.marigoldmailer.example/p/Polar-Nip-Towel-Blue.cfm?tid=338104522

8.https://www.breezecloths.example/

9. http://www.pricedrift.example/cooling-towels/products-html#!

Reason: Due to a massive influx of designs we will be extending the project for four additional days to fairly evaluate all of the designs. No new designs will be considered after today (April 19th). I will be sending out the designs to our network and the one that gets the most votes wins. I really appreciate all of the different designs and will keep you posted on the vote count.

Target Market(s)

16-30, Male, Female, Moms, Dad's and active athletes of all ages

Industry/Entity Type

Clothing

Requirements
Must have
• Simply put I want people to say "whoa..."". When they use the product they say it and instantly buy almost every time. Unfortunately i can't have everyone get to have a free demo. So I need the packaging to convey this and make people feel like it's the party they want to be invited to
Nice to have
• Think Tan Goat and Pebble. Relates to a very wide ranging diverse audience
Should not have
• Not to look stupid, Cartoony or childish. This is not a gimick, it is a great product at a fair price. People have no problem paying for something that works and the packaging needs to reflect the same

```html
<!DOCTYPE html>
<html lang="en">
<head>
<meta charset="utf-8">
<title>Brisk Mist Instant Cooling Towel – Packaging</title>
<link rel="stylesheet" href="https://fonts.googleapis.com/css2?family=Exo+2:wght@300;600&display=swap">
<style>
  :root {
    --stage: #e9eef2;
    --pack-black: #050505;
    --band-white: #ffffff;
    --ice-blue: #4fb3e6;
    --ice-deep: #2a8cc4;
    --ice-text: #7fb9d6;
    --silver: #d9dde0;
    --figure-light: #eaf5fb;
    --figure-deep: #3d86b8;
  }
  html, body { margin: 0; padding: 0; overflow: hidden; }
  body {
    width: 1200px;
    height: 1080px;
    background: var(--stage);
    font-family: "Exo 2", sans-serif;
    position: relative;
  }
  p, h1, h2 { margin: 0; }

  .pack {
    position: absolute;
    background: var(--pack-black);
    overflow: hidden;
    box-shadow: 0 6px 18px rgba(0, 0, 0, 0.25);
  }
  .ice-rule {
    position: absolute;
    left: 0;
    width: 100%;
    height: 3px;
    background: linear-gradient(90deg, rgba(79,179,230,0.15), var(--ice-blue) 30%, var(--ice-deep) 70%, rgba(79,179,230,0.15));
  }
  .ghost-mark {
    position: absolute;
    border-radius: 50%;
    background: radial-gradient(circle at 45% 45%, rgba(5,5,5,1) 0 34%, rgba(120,125,130,0.55) 36%, rgba(90,95,100,0.35) 70%, rgba(60,60,60,0.1) 100%);
  }
  .brand-mark { border-radius: 50%; background: var(--pack-black); }
  .brand-name { color: var(--pack-black); font-weight: 600; }
  .accent {
    background: linear-gradient(180deg, #a8d9f0, #5a9cc2);
    -webkit-background-clip: text;
    background-clip: text;
    color: transparent;
  }

  /* ---------- Tube wrap ---------- */
  .tube { left: 41px; top: 34px; width: 305px; height: 1012px; }
  .tube .tagline {
    position: absolute; top: 56px; left: 0; width: 100%;
    text-align: center; color: var(--silver);
    font-weight: 300; font-size: 24px; letter-spacing: 1px;
  }
  .tube .brand-band {
    position: absolute; top: 216px; left: 0; width: 100%; height: 129px;
    background: var(--band-white);
    display: flex; align-items: center; justify-content: center; gap: 12px;
  }
  .tube .brand-band .ice-rule.top { top: 0; }
  .tube .brand-band .ice-rule.bottom { bottom: 0; }
  .tube .brand-mark { width: 34px; height: 34px; }
  .tube .brand-name { font-size: 38px; letter-spacing: 1px; }
  .tube .product-name {
    position: absolute; top: 396px; left: 0; width: 100%;
    text-align: center; color: #ffffff;
    font-weight: 300; font-size: 46px; line-height: 44px; letter-spacing: 3px;
  }
  .tube .ghost-mark { left: 14px; top: 566px; width: 330px; height: 300px; }
  .tube .activity-row {
    position: absolute; top: 936px; left: 0; width: 100%;
    display: flex; justify-content: center; gap: 26px;
  }
  .tube .activity-figure { width: 64px; height: 64px; }

  /* ---------- Pouch ---------- */
  .pouch { left: 376px; top: 462px; width: 788px; height: 472px; }
  .pouch .brand-band {
    position: absolute; top: 0; left: 0; width: 100%; height: 236px;
    background: var(--band-white);
  }
  .pouch .brand-band .ice-rule.top { top: 8px; }
  .pouch .brand-band .ice-rule.bottom { bottom: 0; }
  .pouch .tagline {
    position: absolute; top: 24px; left: 43px;
    color: #333333; font-weight: 300; font-size: 19px; letter-spacing: 1px;
  }
  .pouch .brand-lockup {
    position: absolute; top: 84px; left: 0; width: 100%;
    display: flex; align-items: center; justify-content: center; gap: 18px;
  }
  .pouch .brand-mark { width: 56px; height: 56px; }
  .pouch .brand-name { font-size: 64px; letter-spacing: 2px; }
  .pouch .ghost-mark { left: 440px; top: 318px; width: 330px; height: 300px; }
  .pouch .product-name {
    position: absolute; top: 250px; left: 0; width: 100%;
    text-align: center; color: #ffffff;
    font-weight: 300; font-size: 54px; letter-spacing: 3px;
  }
  .pouch .activity-row {
    position: absolute; top: 390px; left: 52px;
    display: flex; gap: 16px;
  }
  .pouch .activity-figure { width: 54px; height: 54px; }
</style>
</head>
<body>

  <svg width="0" height="0" style="position:absolute" aria-hidden="true">
    <defs>
      <radialGradient id="figureFill" cx="40%" cy="35%" r="65%">
        <stop offset="0" stop-color="#eaf5fb"/>
        <stop offset="1" stop-color="#3d86b8"/>
      </radialGradient>
    </defs>
  </svg>

  <section class="pack tube">
    <div class="ghost-mark"></div>
    <p class="tagline">SOAK • SHAKE • COOL</p>
    <div class="brand-band">
      <span class="ice-rule top"></span>
      <span class="brand-mark"></span>
      <span class="brand-name">BRISK MIST</span>
      <span class="ice-rule bottom"></span>
    </div>
    <h1 class="product-name">INSTANT<br><span class="accent">COOLING</span><br>TOWEL</h1>
    <div class="activity-row">
      <svg class="activity-figure" viewBox="0 0 62 62" role="img" aria-label="Soccer player silhouette in a blue circle">
        <circle cx="31" cy="31" r="29" fill="url(#figureFill)" stroke="#8fd0ec" stroke-width="2"/>
      </svg>
      <svg class="activity-figure" viewBox="0 0 62 62" role="img" aria-label="Worker with a tool silhouette in a blue circle">
        <circle cx="31" cy="31" r="29" fill="url(#figureFill)" stroke="#8fd0ec" stroke-width="2"/>
      </svg>
      <svg class="activity-figure" viewBox="0 0 62 62" role="img" aria-label="Golfer silhouette in a blue circle">
        <circle cx="31" cy="31" r="29" fill="url(#figureFill)" stroke="#8fd0ec" stroke-width="2"/>
      </svg>
    </div>
  </section>

  <section class="pack pouch">
    <div class="ghost-mark"></div>
    <div class="brand-band">
      <span class="ice-rule top"></span>
      <p class="tagline">SOAK • SHAKE • COOL</p>
      <div class="brand-lockup">
        <span class="brand-mark"></span>
        <span class="brand-name">BRISK MIST</span>
      </div>
      <span class="ice-rule bottom"></span>
    </div>
    <h2 class="product-name">INSTANT <span class="accent">COOLING</span> TOWEL</h2>
    <div class="activity-row">
      <svg class="activity-figure" viewBox="0 0 62 62" role="img" aria-label="Soccer player silhouette in a blue circle">
        <circle cx="31" cy="31" r="29" fill="url(#figureFill)" stroke="#8fd0ec" stroke-width="2"/>
      </svg>
      <svg class="activity-figure" viewBox="0 0 62 62" role="img" aria-label="Worker with a tool silhouette in a blue circle">
        <circle cx="31" cy="31" r="29" fill="url(#figureFill)" stroke="#8fd0ec" stroke-width="2"/>
      </svg>
      <svg class="activity-figure" viewBox="0 0 62 62" role="img" aria-label="Golfer silhouette in a blue circle">
        <circle cx="31" cy="31" r="29" fill="url(#figureFill)" stroke="#8fd0ec" stroke-width="2"/>
      </svg>
    </div>
  </section>

</body>
</html>
```